Water Bottle Design

We are launching a water bottle and need a impactful design.

Target Market(s)

health conscious hipsters

Font styles to use
Sans Serif

Requirements
Must have
• Please include the logo (included) on one side of the bottle and these words on the other side of the bottle. "It’s simple, REUSE this bottle every day. Your action, will REDUCE the amount of waste produced. SAVE your body from drinking the harmful contaminants in your water from Non-BPA plastics. HELP someone else because proceeds from your purchase will help homeless veterans.
• We’re just two dudes that like to drink water and help people. #HandItOn"
• Use a total of two colors
• UPDATE: You do not have to use the bottle on the logo.
Nice to have
• The bottle itself is 34 ounces and looks like a normal water bottle. I will include the image in the files. We would need to be able to change the colors easily.
Should not have
• Do not use more than two colors. Colors should not be important to the design at this point.

```html
<!DOCTYPE html>
<html lang="en">
<head>
<meta charset="utf-8">
<title>Water Bottle Wrap – Front and Back</title>
<link rel="stylesheet" href="https://fonts.googleapis.com/css2?family=Oswald:wght@500;700&family=Questrial&family=Roboto:ital,wght@0,300;0,400;1,400;1,700&display=swap">
<style>
  :root {
    --wrap-blue: #1b93c9;
    --ink-white: #ffffff;
    --label-dark: #1f1f1f;
    --line-dark: #2a2a2a;
    --sheet: #ffffff;
    --art-tint: rgba(255,255,255,0.28);
  }
  * { box-sizing: border-box; margin: 0; padding: 0; }
  html, body { width: 1200px; height: 880px; overflow: hidden; background: var(--sheet); }
  .sheet { position: relative; width: 1200px; height: 880px; }

  .material-label {
    position: absolute; left: 0; width: 1200px; top: 92px; text-align: center;
    font: 500 22px/1 "Oswald", sans-serif; color: var(--label-dark); letter-spacing: 0.3px;
  }
  .material-leaders { position: absolute; left: 0; top: 0; }

  .panel {
    position: absolute; top: 160px; width: 340px; height: 630px;
    background: var(--wrap-blue); color: var(--ink-white); overflow: hidden;
  }
  .panel--front { left: 240px; }
  .panel--back { left: 620px; }

  .side-caption {
    position: absolute; top: 812px; width: 340px; text-align: center;
    font: 500 22px/1 "Oswald", sans-serif; color: var(--label-dark);
  }
  .side-caption--front { left: 240px; }
  .side-caption--back { left: 620px; }

  /* front: brand lockup */
  .brand { position: absolute; left: 0; right: 0; top: 190px; text-align: center; }
  .brand__mark { font: 400 150px/1 "Questrial", sans-serif; letter-spacing: -4px; }
  .brand__line { font: 400 27px/1 "Questrial", sans-serif; margin-top: 6px; opacity: 0.85; }

  /* back: message blocks */
  .block { position: absolute; left: 24px; width: 292px; }
  .head { font-family: "Oswald", sans-serif; font-weight: 700; text-transform: uppercase; line-height: 1; white-space: nowrap; }
  .body { font-family: "Roboto", sans-serif; font-weight: 300; }
  .note { font: italic 400 14px/1.2 "Roboto", sans-serif; }

  .stripe-row { display: flex; align-items: center; gap: 6px; }
  .stripes {
    flex: 1; height: 14px;
    background: repeating-linear-gradient(to bottom, var(--ink-white) 0 2px, transparent 2px 5px);
  }

  .intro { top: 16px; transform: rotate(-4deg); transform-origin: center; text-align: left; }
  .intro__title { font-size: 44px; }
  .intro__reuse { font-size: 24px; }
  .intro__daily { font-size: 23px; line-height: 1.15; white-space: nowrap; }
  .intro__action { font-size: 33px; }

  .reduce-box {
    top: 190px; border: 2px solid var(--ink-white);
    padding: 14px 8px 6px; text-align: center; font-size: 20px; line-height: 1.15;
  }
  .reduce-box__title {
    position: absolute; top: -18px; left: 50%; transform: translateX(-50%);
    background: var(--wrap-blue); padding: 0 6px; font-size: 28px;
  }

  .save { top: 276px; }
  .save__title { font-size: 28px; letter-spacing: 1px; }
  .split { display: flex; align-items: center; gap: 8px; margin-top: 4px; }
  .split .note { flex: 1; }
  .art { flex: none; background: var(--art-tint); }
  .art--bottle { width: 26px; height: 60px; border-radius: 10px 10px 6px 6px; }
  .art--portrait { width: 70px; height: 70px; border-radius: 50%; }
  .art--hand { width: 60px; height: 58px; border-radius: 40% 40% 30% 30%; }

  .help { top: 392px; display: flex; gap: 8px; align-items: center; }
  .help__text { flex: 1; }
  .help__title { font-size: 28px; }
  .help .note { text-align: right; }

  .veterans { top: 480px; font-size: 30px; text-align: center; }
  .closing { top: 522px; display: flex; align-items: center; gap: 10px; padding-left: 20px; }
  .closing .note { font-size: 15px; }
  .closing__tag { font-weight: 700; }
</style>
</head>
<body>
<main class="sheet">
  <p class="material-label">METAL BOTTLE MATERIAL</p>
  <svg class="material-leaders" width="1200" height="200" aria-hidden="true">
    <polyline points="500,160 560,125 640,125 700,160" fill="none" stroke="var(--line-dark)" stroke-width="1.5"/>
  </svg>

  <section class="panel panel--front" aria-label="Front of bottle">
    <div class="brand">
      <p class="brand__mark">HIO</p>
      <p class="brand__line">Hand It On</p>
    </div>
  </section>

  <section class="panel panel--back" aria-label="Back of bottle">
    <div class="block intro">
      <p class="head intro__title">It’s Simple</p>
      <div class="stripe-row"><span class="stripes"></span><span class="head intro__reuse">Reuse</span></div>
      <p class="body intro__daily">this bottle every day.</p>
      <p class="head intro__action">Your action, will</p>
    </div>

    <div class="block reduce-box body">
      <span class="head reduce-box__title">Reduce</span>
      the amount of waste produced.
    </div>

    <div class="block save">
      <div class="stripe-row"><span class="stripes"></span><span class="head save__title">Save</span><span class="stripes"></span></div>
      <div class="split">
        <p class="note">your body from drinking<br>the harmful contaminants<br>in your water from<br>- Non-BPA plastics -</p>
        <div class="art art--bottle" role="img" aria-label="Line drawing of a plastic water bottle"></div>
      </div>
    </div>

    <div class="block help">
      <div class="art art--portrait" role="img" aria-label="Line drawing portrait of a veteran in a cap"></div>
      <div class="help__text">
        <div class="stripe-row"><span class="head help__title">Help</span><span class="stripes"></span></div>
        <p class="note">someone else because<br>proceeds from your<br>purchase will help</p>
      </div>
    </div>

    <p class="block head veterans">Homeless Veterans</p>

    <div class="block closing">
      <p class="note">We’re just two dudes<br>that like to drink water<br>and help people.<br><span class="closing__tag">#HandItOn"</span></p>
      <div class="art art--hand" role="img" aria-label="Line drawing of a hand holding a globe"></div>
    </div>
  </section>

  <p class="side-caption side-caption--front">FRONT</p>
  <p class="side-caption side-caption--back">BACK</p>
</main>
</body>
</html>
```